Business Card Design for an Investment Company

We need a business card design for our private investment company, called Ashbourne Partners. Ashbourne Partners is an investments partnership that aims to acquire shares in listed companies with a view to influencing those companies through active dialogue in order to improve their value. We need designs that use the logo colors (blue, grey, white), we need both English and Arabic on the business cards (can be on one side or 2 sides). The final logo should communicate professionalism, conservatism (nothing too fancy or too cheesy), that we are smart, conservative and old school.

Target Market(s)

Investment companies

Industry/Entity Type

Investment

Contact Information for Business Card

Khalid Yousef Rumaithi
Senior Executive Officer

Palm Terrace 07, Level 3, Office 215/12
HLMZ

+9714987650
krumaithi@ashbournepartners.com
www.ashbournepartners.com

Requirements
Must have
• Logo to be placed on the left hand side of the business card
• for the Arabic, we only need to have the name and title so it can be accomodated on one side so we can have the other side with full color and logo. The arabic that needs to be used is the below:
• خالد يوسف الرميثي
• المدير التنفيدي

```html
<!DOCTYPE html>
<html lang="en">
<head>
<meta charset="utf-8">
<title>Ashbourne Partners – Business Cards</title>
<link rel="stylesheet" href="https://fonts.googleapis.com/css2?family=Montserrat:wght@300;400;500;700&family=Noto+Kufi+Arabic:wght@300;700&display=swap">
<style>
  :root {
    --backdrop: #e4e5e7;
    --card: #f1f2f3;
    --brand-blue: #1f6fa8;
    --brand-grey: #5a5b5d;
    --text-grey: #4a4b4d;
    --white: #ffffff;
  }
  * { box-sizing: border-box; margin: 0; padding: 0; }
  html, body {
    width: 1200px; height: 900px; overflow: hidden;
    background: var(--backdrop);
    font-family: "Montserrat", sans-serif;
  }
  .sheet { position: relative; width: 1200px; height: 900px; }
  .card {
    position: absolute; left: 300px;
    width: 600px; height: 343px;
    background: var(--card);
    box-shadow: 0 6px 18px rgba(0,0,0,.15);
  }
  .card--front { top: 58px; }
  .card--back { top: 478px; }

  .logo {
    position: absolute;
    display: flex; align-items: center; gap: 10px;
    color: var(--brand-blue);
    font-weight: 700; font-size: 30px; letter-spacing: -0.5px;
    white-space: nowrap;
  }
  .logo__mark { width: 14px; height: 14px; background: var(--brand-grey); flex: none; }
  .card--front .logo { left: 50%; top: 50%; transform: translate(-50%, -50%); }
  .card--back .logo { left: 26px; top: 44px; font-size: 26px; }

  .name-band {
    position: absolute; left: 0; top: 112px;
    width: 290px; height: 66px;
    background: var(--brand-grey);
    color: var(--white);
    padding: 13px 0 0 26px;
  }
  .name-band__name { font-weight: 700; font-size: 15px; white-space: nowrap; }
  .name-band__title { font-weight: 300; font-size: 13px; margin-top: 4px; }

  .arabic {
    position: absolute; left: 26px; top: 200px; width: 238px;
    direction: rtl; text-align: right;
    font-family: "Noto Kufi Arabic", sans-serif;
    color: var(--text-grey);
  }
  .arabic__name { font-weight: 700; font-size: 15px; line-height: 1.6; }
  .arabic__title { font-weight: 300; font-size: 13px; line-height: 1.6; }

  .address {
    position: absolute; left: 310px; top: 120px;
    color: var(--text-grey); font-size: 13px; line-height: 1.4; font-weight: 500;
  }
  .contacts {
    position: absolute; left: 290px; top: 198px;
    list-style: none; color: var(--text-grey); font-size: 14px; font-weight: 500;
  }
  .contacts li { display: flex; align-items: center; gap: 10px; height: 24px; white-space: nowrap; }
  .contacts svg { width: 14px; height: 14px; flex: none; }
</style>
</head>
<body>
<main class="sheet">
  <section class="card card--front" aria-label="Card front">
    <div class="logo"><span class="logo__mark"></span>Ashbourne Partners</div>
  </section>

  <section class="card card--back" aria-label="Card back">
    <div class="logo"><span class="logo__mark"></span>Ashbourne Partners</div>

    <div class="name-band">
      <p class="name-band__name">Khalid Yousef Rumaithi</p>
      <p class="name-band__title">Senior Executive Officer</p>
    </div>

    <div class="arabic" lang="ar">
      <p class="arabic__name">خالد يوسف الرميثي</p>
      <p class="arabic__title">المدير التنفيدي</p>
    </div>

    <p class="address">Palm Terrace 07, Level 3,<br>Office 215/12<br>HLMZ</p>

    <ul class="contacts">
      <li>
        <svg viewBox="0 0 16 16" aria-hidden="true"><path d="M4 1.5 6 4.5 4.6 6a8 8 0 0 0 5.4 5.4L11.5 10l3 2-1.5 2.5C7 14 2 9 1.5 3z" fill="none" stroke="var(--brand-blue)" stroke-width="1.3" stroke-linejoin="round"/></svg>
        +9714987650
      </li>
      <li>
        <svg viewBox="0 0 16 16" aria-hidden="true"><rect x="1.5" y="3.5" width="13" height="9" fill="none" stroke="var(--brand-blue)" stroke-width="1.3"/><path d="M1.5 3.5 8 9l6.5-5.5" fill="none" stroke="var(--brand-blue)" stroke-width="1.3"/></svg>
        krumaithi@ashbournepartners.com
      </li>
      <li>
        <svg viewBox="0 0 16 16" aria-hidden="true"><circle cx="8" cy="8" r="6.5" fill="none" stroke="var(--brand-blue)" stroke-width="1.3"/><ellipse cx="8" cy="8" rx="2.8" ry="6.5" fill="none" stroke="var(--brand-blue)" stroke-width="1.1"/><path d="M1.5 8h13" stroke="var(--brand-blue)" stroke-width="1.1"/></svg>
        www.ashbournepartners.com
      </li>
    </ul>
  </section>
</main>
</body>
</html>
```